QRV Supplements needs a label designer for supplement company

Looking for an on going label designer for my supplement company. I have three products that will need designs. I'm about to launch my sleep supplement called Velora Rest and that's the first design needed.
I would like all designs to be somewhat simple, not overstated and uniformed so that when you look at all of the labels of the different supplements they are similar and you can tell it's the same brand.
Please see attached sample pictures below as ideas.
Updates

The brand is QRV supplements, logo file has been provided. The supplement is called Velora Rest. It is a liquid supplement that is a 32/33 ounce white bottle. Die lines and measurements will be provided. Here's text for wording ideas: Wording: Natural Sleep Aid Reset your circadian rhythm. May help you: Fall asleep faster. Get a deeper more restful sleep. Boost Immune System Remember your dreams. Protect your brain and flush toxins. Wake up feeling refreshed. Non-gmo Gluten Free Sugar Free Vegan Manufactured in cGMP factory Manufactured in USA

Target Market(s)

Health and wellness/supplement industry for regular people not hardcore gym goers. My supplements are for a health lifestyle not bodybuilding.

Industry/Entity Type

Health And Wellness

Colors
3176b5
3276b5
33a6d7
85cae6
85abd2
cedeed
e4daeb
b7a5cd

Requirements
Must have
• There will be some text and wording that I will provide that must be on the bottles.

```html
<!DOCTYPE html>
<html lang="en">
<head>
<meta charset="UTF-8">
<title>Velora Rest – QRV Supplements Label</title>
<link href="https://fonts.googleapis.com/css2?family=Oswald:wght@500;700&family=Roboto+Condensed:wght@700&display=swap" rel="stylesheet">
<style>
  :root {
    --page-bg: #ffffff;
    --sky-top: #122649;
    --sky-upper: #1f4a85;
    --sky-mid: #3176b5;
    --sky-light: #85abd2;
    --sky-lilac: #b7a5cd;
    --sky-bottom: #e4daeb;
    --glow-blue: #33a6d7;
    --glow-soft: #cedeed;
    --text-light: #ffffff;
    --text-dark: #172c55;
    --pill-bg: #172c55;
  }
  * { box-sizing: border-box; margin: 0; padding: 0; }
  html, body {
    width: 1200px;
    height: 1142px;
    overflow: hidden;
    background: var(--page-bg);
  }
  .label {
    position: absolute;
    left: 150px;
    top: 41px;
    width: 900px;
    height: 1060px;
    border-radius: 6px;
    background: linear-gradient(180deg,
      var(--sky-top) 0%,
      var(--sky-upper) 30%,
      var(--sky-mid) 58%,
      var(--sky-light) 78%,
      var(--sky-lilac) 90%,
      var(--sky-bottom) 100%);
    display: flex;
    flex-direction: column;
    align-items: center;
    overflow: hidden;
  }
  .brand {
    margin-top: 64px;
    display: flex;
    align-items: center;
    gap: 20px;
  }
  .brand-dot {
    width: 62px;
    height: 62px;
    border-radius: 50%;
    border: 3px solid var(--text-light);
  }
  .brand-name {
    font-family: "Oswald", sans-serif;
    font-weight: 500;
    font-size: 46px;
    color: var(--text-light);
    letter-spacing: 1px;
  }
  .night-art {
    margin-top: 30px;
    width: 620px;
    height: 360px;
    border-radius: 24px;
    background: radial-gradient(ellipse at 65% 45%, rgba(206,222,237,0.45) 0%, rgba(51,166,215,0.2) 45%, rgba(0,0,0,0) 75%);
  }
  .product-name {
    margin-top: 12px;
    text-align: center;
    font-family: "Oswald", sans-serif;
    font-weight: 700;
    color: var(--text-light);
    line-height: 1;
  }
  .product-name .line-one {
    display: block;
    font-size: 112px;
    letter-spacing: 2px;
  }
  .product-name .line-two {
    display: block;
    font-size: 128px;
    letter-spacing: 72px;
    margin-right: -72px;
    margin-top: 4px;
  }
  .tagline {
    margin-top: 30px;
    text-align: center;
    font-family: "Roboto Condensed", sans-serif;
    font-weight: 700;
    font-size: 42px;
    line-height: 1.2;
    color: var(--text-dark);
  }
  .feature {
    margin-top: 12px;
    display: flex;
    align-items: center;
    gap: 16px;
    font-family: "Roboto Condensed", sans-serif;
    font-weight: 700;
    font-size: 40px;
    color: var(--text-dark);
  }
  .feature-rule {
    width: 80px;
    height: 5px;
    background: var(--text-dark);
  }
  .contents-pill {
    position: absolute;
    bottom: 0;
    left: 50%;
    transform: translateX(-50%);
    padding: 8px 40px 12px;
    border-radius: 30px 30px 0 0;
    background: var(--pill-bg);
    font-family: "Roboto Condensed", sans-serif;
    font-weight: 700;
    font-size: 34px;
    color: var(--text-light);
    white-space: nowrap;
  }
</style>
</head>
<body>
  <main class="label">
    <header class="brand">
      <span class="brand-dot"></span>
      <span class="brand-name">QRV SUPPLEMENTS</span>
    </header>

    <div class="night-art" role="img" aria-label="Starry night sky with a glowing crescent moon and a line-drawn sleeping brain with floating Zzz"></div>

    <h1 class="product-name">
      <span class="line-one">VELORA</span>
      <span class="line-two">REST</span>
    </h1>

    <p class="tagline">Reset Your Circadian Rhythm So You<br>Wake Up Feeling Refreshed</p>

    <p class="feature">
      <span class="feature-rule"></span>
      NATURAL SLEEP AID
      <span class="feature-rule"></span>
    </p>

    <p class="contents-pill">Dietary Supplement - 32 fl oz LIQUID</p>
  </main>
</body>
</html>
```